Stationery for a private security company, "Brennock Security Services Ltd."

Needed is a stationery design for a private security company. The designs must show professionalism and that our company mean nothing but business. Watermark of the company logo on the letterhead page is also a must. The final design must represent innovation and professionalism. It would be great if designers could integrate the colours black and silver onto the cards and letterheads..

Thank you

```html
<!DOCTYPE html>
<html lang="en">
<head>
<meta charset="utf-8">
<title>Brennock Security Services Ltd. — Stationery</title>
<link rel="stylesheet" href="https://fonts.googleapis.com/css2?family=Montserrat:wght@600&family=Open+Sans:wght@400;600&family=Orbitron:wght@500&display=swap">
<style>
  :root {
    --backdrop: #5a5a5a;
    --paper: #ffffff;
    --ink: #1c1c1c;
    --steel-dark: #2b2b2b;
    --steel-mid: #8e9094;
    --steel-light: #d9dadc;
    --watermark: #e2e2e2;
    --rule: #ececec;
  }
  * { margin: 0; padding: 0; box-sizing: border-box; }
  html, body { width: 848px; height: 1200px; overflow: hidden; }
  body { background: var(--backdrop); position: relative; font-family: "Open Sans", sans-serif; }

  .letterhead {
    position: absolute; left: 78px; top: 80px; width: 540px; height: 780px;
    background: var(--paper); overflow: hidden;
  }
  .letterhead__band { position: absolute; left: 0; top: 0; width: 100%; height: 150px; }
  .brand {
    position: absolute; left: 0; right: 0; top: 34px;
    display: flex; flex-direction: column; align-items: center; color: var(--ink);
  }
  .brand__mark { width: 16px; height: 16px; border-radius: 50%; background: var(--ink); margin-bottom: 6px; }
  .brand__name { font-family: "Montserrat", sans-serif; font-weight: 600; font-size: 22px; letter-spacing: 2px; line-height: 1; }
  .brand__sub { font-family: "Montserrat", sans-serif; font-weight: 600; font-size: 8.5px; letter-spacing: .5px; margin-top: 3px; }

  .letterhead__watermark {
    position: absolute; left: 60px; top: 400px; transform: rotate(-16deg); transform-origin: left top;
    color: var(--watermark); font-family: "Montserrat", sans-serif; font-weight: 600;
  }
  .watermark__circle { width: 90px; height: 90px; border-radius: 50%; background: var(--watermark); margin: 0 0 14px 150px; }
  .watermark__name { font-size: 64px; letter-spacing: 7px; line-height: 1; }
  .watermark__sub { font-size: 24px; letter-spacing: 2px; margin-top: 4px; }

  .letterhead__rule { position: absolute; left: 0; width: 100%; }
  .letterhead__rule--mid { top: 435px; height: 10px; background: linear-gradient(90deg, var(--rule), #f6f6f6 60%, var(--rule)); transform: rotate(-1deg); }
  .letterhead__footer { position: absolute; left: 0; bottom: 0; width: 100%; height: 52px;
    background: linear-gradient(180deg, #f1f1f1 0, #dcdcdc 30%, #f4f4f4 60%, #e6e6e6 100%); }

  .card {
    position: absolute; left: 430px; top: 905px; width: 360px; height: 205px; overflow: hidden;
    background: linear-gradient(115deg, #4a4b4e 0%, #b9babd 30%, #e4e5e7 55%, #9c9da1 80%, #6b6c70 100%);
    color: var(--ink);
  }
  .card__band { position: absolute; left: 0; top: 0; width: 100%; height: 70px; }
  .card .brand { top: 14px; left: 120px; right: 0; }
  .card .brand__mark { width: 10px; height: 10px; margin-bottom: 3px; }
  .card .brand__name { font-size: 14px; letter-spacing: 1.5px; }
  .card .brand__sub { font-size: 6px; }
  .card__person { position: absolute; left: 22px; top: 82px; }
  .card__name { font-family: "Orbitron", sans-serif; font-weight: 500; font-size: 17px; letter-spacing: 1.5px; }
  .card__email { font-size: 8px; margin-top: 6px; }
  .card__contact { position: absolute; left: 22px; top: 148px; font-size: 7.5px; line-height: 1.7; }
</style>
</head>
<body>
  <section class="letterhead" aria-label="Letterhead">
    <svg class="letterhead__band" viewBox="0 0 540 150" preserveAspectRatio="none" aria-hidden="true">
      <defs>
        <linearGradient id="steel" x1="0" x2="1" y1="0" y2="0">
          <stop offset="0" stop-color="#2b2b2b"/>
          <stop offset=".3" stop-color="#9a9b9f"/>
          <stop offset=".55" stop-color="#e3e4e6"/>
          <stop offset=".8" stop-color="#8e9094"/>
          <stop offset="1" stop-color="#3a3a3c"/>
        </linearGradient>
      </defs>
      <path d="M0 0 H540 V82 Q270 150 0 90 Z" fill="url(#steel)"/>
      <path d="M0 108 Q270 122 540 80 V92 Q270 134 0 120 Z" fill="#d6d7d9" opacity=".8"/>
    </svg>
    <div class="brand">
      <span class="brand__mark"></span>
      <span class="brand__name">BRENNOCK</span>
      <span class="brand__sub">Security Services Ltd.</span>
    </div>
    <div class="letterhead__rule letterhead__rule--mid"></div>
    <div class="letterhead__watermark" aria-hidden="true">
      <div class="watermark__circle"></div>
      <div class="watermark__name">BRENNOCK</div>
      <div class="watermark__sub">SECURITY SERVICES LTD.</div>
    </div>
    <div class="letterhead__footer"></div>
  </section>

  <section class="card" aria-label="Business card">
    <svg class="card__band" viewBox="0 0 360 70" preserveAspectRatio="none" aria-hidden="true">
      <path d="M0 0 H360 V40 Q180 75 0 30 Z" fill="#3b3c3f" opacity=".55"/>
      <path d="M0 20 Q180 70 360 48 V55 Q180 78 0 27 Z" fill="#d9dadc" opacity=".7"/>
    </svg>
    <div class="brand">
      <span class="brand__mark"></span>
      <span class="brand__name">BRENNOCK</span>
      <span class="brand__sub">Security Services Ltd.</span>
    </div>
    <div class="card__person">
      <p class="card__name">DANIEL HART</p>
      <p class="card__email">d.hart@brennocksecurity.com</p>
    </div>
    <div class="card__contact">
      <p>Tel. 0145 772390, Mob. 07911 503118</p>
      <p>Corporate, 128 Orchard St, Halden City, NY 12534</p>
    </div>
  </section>
</body>
</html>
```